hobby beef jerky maker looking to break into the commercial market

We need product labels designed for each flavour of jerky we make. Currently have 3 flavours that we are ready to share with the world. We need in your face designs to help us stand out from an already crowded market.
The product name is Rivet Beef Jerky.
The flavours we offer have been named Porch Lope, Ember Glaze and Chili Knack.
The Rivet Beef Jerky Title should remain the same across the three labels but the design for each flavour can change as you see fit.
Label needs to fit within 110mm x 110mm to suit our current packaging

Industry/Entity Type

Food Production

Logo Text

Morvendale Apiary

Colors

Designer to choose colors to be used in the design.

Requirements
Must have
• "Rivet Beef Jerky" font and colour must remain the same across the 3 designs
Nice to have
• The labels will be used on the clear side of the packaging with a small space towards the bottom being left visible so the product inside can be seen

```html
<!DOCTYPE html>
<html lang="en">
<head>
<meta charset="utf-8">
<title>Rivet Beef Jerky – Flavour Labels</title>
<link href="https://fonts.googleapis.com/css2?family=Oswald:wght@500;700&display=swap" rel="stylesheet">
<style>
  :root {
    --backdrop: #e6caa0;
    --label-dark: #25140f;
    --ink-light: #ffffff;
    --ink-dark: #231712;
    --chili: #c0071b;
    --porch: #7dc21f;
    --ember: #ea0a8c;
  }
  * { box-sizing: border-box; margin: 0; padding: 0; }
  html, body { width: 1200px; height: 646px; overflow: hidden; }
  body {
    background: var(--backdrop);
    font-family: "Oswald", "Arial Narrow", sans-serif;
    position: relative;
  }
  .label {
    position: absolute;
    top: 142px;
    width: 333px;
    height: 332px;
    background: var(--label-dark);
    border-radius: 10px;
    overflow: hidden;
  }
  .label--chili { left: 77px; --band: var(--chili); }
  .label--porch { left: 446px; --band: var(--porch); }
  .label--ember { left: 814px; --band: var(--ember); }

  .brand-dot {
    position: absolute;
    left: 111px;
    top: 30px;
    width: 110px;
    height: 110px;
    border-radius: 50%;
    background: var(--ink-light);
  }
  .brand-name {
    position: absolute;
    left: 0;
    right: 0;
    top: 160px;
    text-align: center;
    color: var(--ink-light);
    font-weight: 700;
    font-size: 34px;
    line-height: 44px;
    letter-spacing: 1px;
    text-transform: uppercase;
    white-space: nowrap;
  }
  .flavour-band {
    position: absolute;
    left: 0;
    top: 0;
    width: 333px;
    height: 332px;
  }
  .flavour-band path { fill: var(--band); }
  .flavour-name {
    position: absolute;
    left: 0;
    right: 0;
    top: 250px;
    text-align: center;
    color: var(--ink-dark);
    font-weight: 500;
    font-size: 30px;
    line-height: 40px;
    letter-spacing: 2px;
    text-transform: uppercase;
    white-space: nowrap;
  }
  .net-weight {
    position: absolute;
    left: 0;
    right: 0;
    top: 303px;
    text-align: center;
    color: var(--ink-light);
    font-weight: 500;
    font-size: 11px;
    line-height: 14px;
    letter-spacing: 0.5px;
    text-transform: uppercase;
  }
</style>
</head>
<body>

  <section class="label label--chili">
    <span class="brand-dot" aria-hidden="true"></span>
    <p class="brand-name">Rivet Beef Jerky</p>
    <svg class="flavour-band" viewBox="0 0 333 332" aria-hidden="true">
      <path d="M0,238 Q166,250 333,238 L333,300 Q166,290 0,300 Z"/>
    </svg>
    <h2 class="flavour-name">Chili Knack</h2>
    <p class="net-weight">Net Wt. 50g</p>
  </section>

  <section class="label label--porch">
    <span class="brand-dot" aria-hidden="true"></span>
    <p class="brand-name">Rivet Beef Jerky</p>
    <svg class="flavour-band" viewBox="0 0 333 332" aria-hidden="true">
      <path d="M0,238 Q166,250 333,238 L333,300 Q166,290 0,300 Z"/>
    </svg>
    <h2 class="flavour-name">Porch Lope</h2>
    <p class="net-weight">Net Wt. 50g</p>
  </section>

  <section class="label label--ember">
    <span class="brand-dot" aria-hidden="true"></span>
    <p class="brand-name">Rivet Beef Jerky</p>
    <svg class="flavour-band" viewBox="0 0 333 332" aria-hidden="true">
      <path d="M0,238 Q166,250 333,238 L333,300 Q166,290 0,300 Z"/>
    </svg>
    <h2 class="flavour-name">Ember Glaze</h2>
    <p class="net-weight">Net Wt. 50g</p>
  </section>

</body>
</html>
```